1 Simple Menu Board Design For Ice Cream Shop

We are a shaved ice shop that needs ONE menu board designed with 6 pre-set shaved ice combinations. This is a very simple project where I will give you all the images and text you need for the menu board.

Requirements:
1) I need the photoshop or illustrator file after you are finished (in case we need to make minor tweaks in the future). If you win, I will give you a site for you to ftp the final photoshop or illustrator file. (Adobe Photoshop or Illustrator only!)
2) Menu board design dimensions must be 9,600 pixels height x 5,400 pixels wide (want it large so can print on large posters if needed in the future)
3) Design must "fit" with our existing menu board designs, but of course look professional. But do NOT be bound by our previous menu boards. If you have a BETTER more exciting/stylish/classy design in your head, go for it.
4) The 6 ice combos should FILL up the entire menu board. Don't want too much "empty" background space around pictures. The ICE should be stars of the board. Please take a look at "[login to view URL]" for format we would like the menu board to look.
5) Please use the [login to view URL] file as the background file for this menu board. But only use right half side.
**** UPDATE: PLEASE TAKE A LOOK AT "[login to view URL]" for what we hope the ice combo menu board to look like. Please tastefully crop the ice pics to fit into the boxes. The titles ie: "1 Vanilla Milk" should be placed under the picture of the ice.

Design Criteria:

- Top of menu board should say "Popular Ice Combos" in a classy way. Please don't tweak text into wavy shapes, or other cheesy shapes. Do NOT write the title "vela ice" or any other title on this menu board besides "Popular Ice Combos".
- 6 combos on menu board. 3 Rows x 2 columns of combos each should FILL UP menu board. DON'T rotate the 6 boxes.
- When scaled, Text size should be approximately same size as the text in Vela2-Menu1 file.
- Probably best if ice pictures cropped out, and if needed black backgrounds replaced with a tasteful "blurred" background
- A clear cropped picture of each ice combo with the name of the combo (larger font), and under the combo name, a description of what is included in the combo (smaller font) should be included.
- Each ice combo needs the NUMBER written somewhere so people can call the combo by number (1,2..6) Don't just write "Vanilla Milk". etc..
- Ice descriptions/Toppings should be all in lower case
- Layout of ice on board should look like the following:
#1 #2
#3 #4
#5 #6

These are the combos and descriptions:
#1 Vanilla Milk (strawberries, crunkets, condensed milk, chocolate drizzle)
#2 Green Tea (flan pudding, red bean, condensed milk)
#3 Sea Salt Caramel (almond slices, crunkets, caramel drizzle)
#4 Strawberry (boba, strawberry jelly, Strawberry drizzle)
#5 Chocolate (b&ts, marshmallows, chocolate drizzle)
#6 Coconut (rainbow jelly, mango poppers, mango drizzle)

Will be Given:
Attached are the 6 images of the combinations, which you will need to crop and fit on the menu board. Preferably don't use the dark black background colors from the photos of the ice, as the black colors don't seem to fit with the other menu board feel. A tasteful "blurred" background can be used to fill up empty space behind ice if needed for each square. Again, This menu board I need you to design will be on the right half of the file [login to view URL], and must blend well wight the left half image.

Also attached are other menu boards that we currently have and the feel we want the menu board to blend with.

Please submit your design on top of the file "[login to view URL]", where I can see the existing left side design, and your new right side combo design.

```html
<!DOCTYPE html>
<html lang="en">
<head>
<meta charset="utf-8">
<title>vela ice – Menu Board</title>
<link href="https://fonts.googleapis.com/css2?family=Arimo:wght@400;700&family=Archivo+Narrow:wght@400&family=Pathway+Gothic+One&family=Luckiest+Guy&display=swap" rel="stylesheet">
<style>
  :root{
    --sky-light:#e6f6fd;
    --sky-mid:#b9e3f6;
    --sky-deep:#6fc1ea;
    --brand-blue:#1c7dc3;
    --flavor-blue:#2b86c7;
    --ink:#10223a;
    --magenta:#d8237f;
    --magenta-deep:#a8145e;
    --orange:#e8641e;
    --title-orange:#e9945a;
    --white:#ffffff;
  }
  *{margin:0;padding:0;box-sizing:border-box}
  html,body{width:1200px;height:1067px;overflow:hidden}
  body{font-family:"Arimo",Arial,sans-serif;background:var(--sky-light)}
  .board{position:relative;width:1200px;height:1067px;overflow:hidden;
    background:linear-gradient(90deg,var(--sky-light) 0%,#d6f0fb 48%,var(--sky-mid) 52%,#a4d9f2 100%);}
  .board::after{content:"";position:absolute;left:600px;right:0;bottom:0;height:120px;
    background:linear-gradient(180deg,rgba(111,193,234,0),var(--sky-deep));}

  /* left panel */
  .brand{position:absolute;left:62px;top:60px;display:flex;align-items:center;gap:18px}
  .brand-name{font-family:"Arimo",Arial,sans-serif;font-weight:700;font-size:96px;color:var(--brand-blue);letter-spacing:-2px;line-height:1;white-space:nowrap}
  .brand-dot{width:34px;height:34px;background:var(--magenta);border-radius:50%}
  .tagline{position:absolute;left:135px;top:186px;font-size:31px;color:var(--brand-blue);white-space:nowrap}
  .sizes{position:absolute;left:90px;top:256px;font-size:25px;color:var(--ink);line-height:32px}
  .sizes .row{display:flex}
  .sizes .label{width:200px}
  .sizes .indent{padding-left:83px;width:200px}
  .sizes .price{color:var(--magenta)}
  .badge{position:absolute;left:416px;top:234px;width:146px;height:146px;border-radius:50%;
    background:var(--magenta);display:flex;align-items:center;justify-content:center;
    font-family:"Luckiest Guy",sans-serif;color:var(--white);font-size:20px;line-height:24px;text-align:center;transform:rotate(-12deg);white-space:nowrap}
  .flavors-title{position:absolute;left:71px;top:334px;font-size:25px;line-height:29px;font-weight:700;color:var(--ink)}
  .flavors{position:absolute;top:364px;list-style:none;font-size:25px;color:var(--flavor-blue)}
  .flavors li{height:29px;line-height:29px;white-space:nowrap}
  .flavors.col-a{left:71px}
  .flavors.col-b{left:311px}
  .fruit{color:var(--magenta);font-size:20px;line-height:1}
  .note{position:absolute;left:71px;top:570px;font-size:20px;line-height:24px;color:var(--ink);white-space:nowrap}
  .pick{position:absolute;left:78px;top:598px;font-size:26px;line-height:30px;color:var(--ink);white-space:nowrap}
  .order-banner{position:absolute;left:113px;top:643px;width:374px;height:42px;border-radius:21px;
    background:var(--magenta);border:2px solid var(--white);color:var(--white);
    font-family:"Luckiest Guy",sans-serif;font-size:18px;display:flex;align-items:center;justify-content:center;white-space:nowrap}
  .arrow{position:absolute;top:637px;width:82px;height:84px}
  .arrow.left{left:22px}
  .arrow.right{left:498px}
  .feature-photo{position:absolute;left:0;top:727px;width:600px;height:340px;
    background:linear-gradient(90deg,#9aae6c 0%,#e89a5a 30%,#f2e6d6 62%,#cfe9f6 100%)}

  /* right panel */
  .combos-title{position:absolute;left:612px;top:96px;width:588px;text-align:center;white-space:nowrap;
    font-family:"Pathway Gothic One",sans-serif;font-size:78px;color:var(--title-orange);line-height:1}
  .combo{position:absolute;width:286px}
  .combo-photo{height:193px}
  .combo-label{margin-top:4px;border:2px solid var(--white);background:var(--white)}
  .combo-head{background:var(--orange);height:32px;display:flex;align-items:center;position:relative}
  .combo-num{position:absolute;left:6px;top:1px;width:28px;height:28px;border:2px solid var(--white);border-radius:50%;
    color:var(--white);font-size:19px;display:flex;align-items:center;justify-content:center}
  .combo-name{flex:1;text-align:center;color:#ffe9d6;font-size:22px;padding-left:20px;white-space:nowrap}
  .combo-desc{height:30px;display:flex;align-items:center;justify-content:center;white-space:nowrap;
    font-family:"Archivo Narrow","Arial Narrow",sans-serif;font-size:12.5px;color:#111;text-transform:lowercase}
  .c1{left:611px;top:200px}.c2{left:911px;top:200px}
  .c3{left:611px;top:473px}.c4{left:911px;top:473px}
  .c5{left:611px;top:738px}.c6{left:911px;top:738px}
  .c1 .combo-photo{background:radial-gradient(ellipse at 55% 55%,#f4efe6 0%,#8a5a3c 45%,#c9e8f6 75%)}
  .c2 .combo-photo{background:radial-gradient(ellipse at 55% 50%,#a9c77a 0%,#8aaa5a 40%,#c9e8f6 75%)}
  .c3 .combo-photo{background:radial-gradient(ellipse at 55% 55%,#f1e4cc 0%,#c99a62 40%,#c9e8f6 75%)}
  .c4 .combo-photo{background:radial-gradient(ellipse at 55% 55%,#f3c6cf 0%,#d8384e 42%,#c9e8f6 75%)}
  .c5 .combo-photo{background:radial-gradient(ellipse at 55% 55%,#9b6a4c 0%,#6b4430 40%,#c9e8f6 75%)}
  .c6 .combo-photo{background:radial-gradient(ellipse at 55% 55%,#fbf2d8 0%,#f2b632 42%,#c9e8f6 75%)}
</style>
</head>
<body>
<main class="board">
  <section class="menu-left">
    <div class="brand"><span class="brand-name">vela ice</span><span class="brand-dot"></span></div>
    <p class="tagline">Artisanal Shaved Ice</p>
    <div class="sizes">
      <div class="row"><span class="label">Sizes: Hill</span><span class="price">5</span></div>
      <div class="row"><span class="indent">Mountain</span><span class="price">7</span></div>
    </div>
    <div class="badge">CUSTOMIZE<br>YOUR ICE</div>
    <h2 class="flavors-title">Ice Flavors:</h2>
    <ul class="flavors col-a">
      <li>Vanilla Milk</li><li>Sea Salt Caramel</li><li>Almond</li><li>Chocolate</li>
      <li>Strawberry <span class="fruit">✻</span></li><li>Coconut <span class="fruit">✻</span></li><li>Lychee <span class="fruit">✻</span></li>
    </ul>
    <ul class="flavors col-b">
      <li>Green Tea</li><li>Coffee</li><li>Taro</li><li>Peanut Butter</li>
      <li>Mango <span class="fruit">✻</span></li><li>Durian <span class="fruit">✻</span></li>
    </ul>
    <p class="note"><span class="fruit">✻</span> = fruit ice additional 0.50(H) / 0.75(M)</p>
    <p class="pick">Pick Your <b>Toppings</b> and <b>Drizzle</b></p>
    <svg class="arrow left" viewBox="0 0 82 84"><path d="M20 2h42v40h18L41 82 2 42h18z" fill="var(--magenta)" stroke="var(--magenta-deep)" stroke-width="2"/></svg>
    <div class="order-banner">GET YOUR ICE ORDER FORM BELOW</div>
    <svg class="arrow right" viewBox="0 0 82 84"><path d="M20 2h42v40h18L41 82 2 42h18z" fill="var(--magenta)" stroke="var(--magenta-deep)" stroke-width="2"/></svg>
    <div class="feature-photo" role="img" aria-label="Photo of green tea shaved ice with strawberries and mango beside vanilla shaved ice with boba"></div>
  </section>

  <section class="menu-right">
    <h1 class="combos-title">Popular Ice Combos</h1>
    <article class="combo c1"><div class="combo-photo" role="img" aria-label="Vanilla milk shaved ice with strawberries and chocolate drizzle"></div>
      <div class="combo-label"><div class="combo-head"><span class="combo-num">1</span><span class="combo-name">Vanilla Milk</span></div><div class="combo-desc">strawberries, crunkets, condensed milk, chocolate drizzle</div></div></article>
    <article class="combo c2"><div class="combo-photo" role="img" aria-label="Green tea shaved ice with flan pudding and red bean"></div>
      <div class="combo-label"><div class="combo-head"><span class="combo-num">2</span><span class="combo-name">Green Tea</span></div><div class="combo-desc">flan pudding, red bean, condensed milk</div></div></article>
    <article class="combo c3"><div class="combo-photo" role="img" aria-label="Sea salt caramel shaved ice with almond slices and caramel drizzle"></div>
      <div class="combo-label"><div class="combo-head"><span class="combo-num">3</span><span class="combo-name">Sea Salt Caramel</span></div><div class="combo-desc">almond slices, crunkets, caramel drizzle</div></div></article>
    <article class="combo c4"><div class="combo-photo" role="img" aria-label="Strawberry shaved ice with boba and strawberry jelly"></div>
      <div class="combo-label"><div class="combo-head"><span class="combo-num">4</span><span class="combo-name">Strawberry</span></div><div class="combo-desc">boba, strawberry jelly, strawberry drizzle</div></div></article>
    <article class="combo c5"><div class="combo-photo" role="img" aria-label="Chocolate shaved ice with candies and marshmallows"></div>
      <div class="combo-label"><div class="combo-head"><span class="combo-num">5</span><span class="combo-name">Chocolate</span></div><div class="combo-desc">b&amp;ts, marshmallows, chocolate drizzle</div></div></article>
    <article class="combo c6"><div class="combo-photo" role="img" aria-label="Coconut shaved ice with rainbow jelly and mango poppers"></div>
      <div class="combo-label"><div class="combo-head"><span class="combo-num">6</span><span class="combo-name">Coconut</span></div><div class="combo-desc">rainbow jelly, mango poppers, mango drizzle</div></div></article>
  </section>
</main>
</body>
</html>
```